Need a stunning home page for Car rental company

For a client, I need a slick and sumber home page design. It is a small, local car rental company, with a handful of cars available for rent.
Selling points: affordable lease, availability, always clean cars
The design should be:
- flat and modern
- no, or very few animations/sliders
- CTA: booking form for renting a car.
- 3 featured cars with images and facts (see website) with button to read more about the car.
- fullscreen background video can be an option
- main colour: #efba01
The site is under construction here:
http://tavnumobil.kessvira.no/
Delivery requirements:
I need a layered & well organised PSD file delivered.

```html
<!DOCTYPE html>
<html lang="no">
<head>
<meta charset="utf-8">
<title>Tavnum Bilutleie</title>
<link rel="stylesheet" href="https://fonts.googleapis.com/css2?family=Montserrat:wght@400;600;700&family=Varela+Round&family=Ubuntu:wght@500&display=swap">
<style>
:root{
  --gold:#e8b400;
  --gold-dark:#c99a00;
  --title-gold:#c8960a;
  --text:#666;
  --dark:#3a3a3a;
  --nav:#a59c96;
  --blue:#1d2aa8;
  --footer:#232427;
  --footer-bottom:#1b1c1e;
  --page:#ececec;
}
*{margin:0;padding:0;box-sizing:border-box}
html,body{width:958px;height:1200px;overflow:hidden}
body{position:relative;background:var(--page);font-family:"Varela Round",sans-serif;color:var(--text)}
.abs{position:absolute}
/* header */
.header{left:0;top:0;width:958px;height:86px;background:#f4f4f4}
.logo{left:100px;top:30px;font-family:"Montserrat",sans-serif;font-weight:700;font-size:22px;letter-spacing:1px;color:var(--gold)}
.search{left:570px;top:30px;width:152px;height:24px;border:1px solid #ccc;border-radius:12px;background:#fff;font-size:10px;color:#bbb;padding:6px 0 0 13px}
.search svg{position:absolute;right:10px;top:5px}
.phone{left:752px;top:24px;font-family:"Montserrat",sans-serif;font-size:17px;color:#1b2a6e;display:flex;align-items:center;gap:6px}
.phone-ico{width:15px;height:15px;background:var(--gold);border-radius:3px;display:flex;align-items:center;justify-content:center}
.call{left:766px;top:48px;font-family:"Montserrat",sans-serif;font-size:15px;color:#555}
/* nav */
.nav{left:0;top:87px;width:958px;height:43px;background:linear-gradient(#b4aca7,#9c938e);border-top:1px solid #ccc;display:flex;padding-left:103px}
.nav a{font-family:"Montserrat",sans-serif;color:#fff;text-decoration:none;font-size:14px;height:43px;line-height:43px;border-left:1px solid #8a817c;text-align:center}
.nav a:last-child{border-right:1px solid #8a817c}
/* hero */
.hero{left:0;top:130px;width:958px;height:334px;background:linear-gradient(100deg,#7c8a55 0%,#a89b86 25%,#b9b2a4 45%,#8e8577 65%,#6a6a5e 100%)}
.hero-shade{left:0;top:130px}
.hero-title{left:691px;top:328px;font-family:"Montserrat",sans-serif;font-weight:700;font-size:15px;color:#fff}
.hero-sub{left:691px;top:351px;font-family:"Montserrat",sans-serif;font-size:9px;color:#fff}
.arrow{top:374px;width:27px;height:24px;background:#fff;display:flex;align-items:center;justify-content:center}
.dots{left:768px;top:384px;display:flex;gap:4px}
.dots span{width:6px;height:6px;border-radius:50%;background:#ccc}
.dots span.on{background:#1d2aa8}
/* welcome */
.welcome{left:102px;top:484px;width:495px;height:201px;background:#fff;padding:22px 14px 0 14px;box-shadow:0 0 2px #ddd}
.welcome h1{font-weight:400;font-size:17px;color:var(--title-gold);margin-bottom:17px}
.welcome p{font-size:11px;line-height:15.5px;margin:0 2px 11px}
/* booking */
.book{left:616px;top:484px;width:239px;height:191px;background:#fff;border-radius:4px;box-shadow:0 8px 8px -6px rgba(0,0,0,.25)}
.book-head{height:40px;background:linear-gradient(90deg,#1c2bb0,#1020a0 60%,#3a4ad0);border-radius:4px 4px 0 0;color:#fff;font-family:"Montserrat",sans-serif;font-weight:600;font-size:16px;padding:11px 15px}
.step{width:17px;height:17px;border:1px solid #888;border-radius:50%;font-size:11px;text-align:center;line-height:15px;color:#777}
.lbl{font-family:"Montserrat",sans-serif;font-weight:600;font-size:11px;color:#555}
.field{height:13px;border:1px solid #e4e4e4;font-size:5px;color:#bbb;padding:3px 8px}
.btn{background:var(--gold);color:#fff;font-family:"Montserrat",sans-serif;font-weight:700;text-align:center;border-bottom:2px solid var(--gold-dark)}
/* cards */
.card{top:715px;width:240px;height:291px;background:#fff;border-radius:3px}
.card-photo{width:240px;height:123px;background:linear-gradient(180deg,#a8b6c2 0%,#e2e4e6 30%,#d5d7d8 60%,#8c8c8a 100%);border-radius:3px 3px 0 0}
.card h2{font-family:"Montserrat",sans-serif;font-weight:600;font-size:10px;color:var(--gold);text-align:center;margin:10px 10px 0;padding-bottom:5px;border-bottom:1px solid #ddd}
.specs{margin:9px 0 0 32px;font-size:7px;border-collapse:collapse}
.specs td{height:12px;color:#666}
.specs td:first-child{width:135px}
.specs td:last-child{font-family:"Montserrat",sans-serif;font-weight:600;color:#444}
.card .btn{position:absolute;left:84px;top:267px;width:73px;height:17px;font-size:8px;line-height:16px}
/* footer */
.footer{left:0;top:1026px;width:958px;height:146px;background:var(--footer)}
.fh{top:1042px;font-family:"Ubuntu",sans-serif;font-weight:500;font-size:12px;color:#fff}
.video{left:193px;top:1050px;width:98px;height:49px;background:linear-gradient(90deg,#6b6a4e,#9a8870 50%,#6a4a3e)}
.ftxt{font-size:5px;line-height:9px;color:#fff}
.input{left:367px;width:92px;background:#ddd;font-size:5px;color:#999;padding:3px 7px;font-style:italic}
.news{left:522px;width:110px;border-bottom:1px solid #3a8a8a;padding-bottom:6px;display:flex;gap:5px}
.date{width:21px;height:20px;background:#fff;text-align:center;font-size:7px;color:#245}
.date b{display:block;background:var(--gold);font-size:5px;font-weight:400;color:#333;height:7px}
.social{left:684px;font-family:"Montserrat",sans-serif;font-size:8px;color:#fff;width:70px;display:flex;justify-content:space-between;align-items:center}
.social i{width:10px;height:9px;display:block}
.bottom{left:0;top:1172px;width:958px;height:28px;background:var(--footer-bottom)}
.bottom-nav{left:104px;top:1184px;display:flex;gap:23px;font-family:"Montserrat",sans-serif;font-size:6.5px;color:#fff}
.copy{left:719px;top:1183px;font-size:5.5px;color:#ccc}
</style>
</head>
<body>
<div class="abs header"></div>
<div class="abs logo">TAVNUMBILUTLEIE</div>
<div class="abs search">Search site
  <svg width="12" height="12" viewBox="0 0 12 12"><circle cx="5" cy="5" r="3.6" fill="none" stroke="#bbb" stroke-width="1.5"/><line x1="7.6" y1="7.6" x2="11" y2="11" stroke="#bbb" stroke-width="1.8"/></svg>
</div>
<div class="abs phone"><span class="phone-ico"><svg width="9" height="9" viewBox="0 0 10 10"><path d="M2 1l2 2-1 1.3c.6 1.2 1.5 2.1 2.7 2.7L7 6l2 2-1.3 1.3C4.8 9 1 5.2.7 2.3z" fill="#fff"/></svg></span>40 12 39 87</div>
<div class="abs call">Call Us Now</div>

<nav class="abs nav">
  <a href="#" style="width:92px">HJEM</a>
  <a href="#" style="width:168px">BILPARKEN VÅR</a>
  <a href="#" style="width:133px">TJENESTER</a>
  <a href="#" style="width:152px">KONTAKT OSS</a>
  <a href="#" style="width:87px">BLOG</a>
  <a href="#" style="width:117px">ABOUT US</a>
</nav>

<div class="abs hero" role="img" aria-label="Red convertible car parked on a mountain road in front of a rocky cliff"></div>
<svg class="abs hero-shade" width="958" height="334" viewBox="0 0 958 334"><polygon points="820,0 958,0 958,334 590,334" fill="rgba(20,20,22,.72)"/></svg>
<div class="abs hero-title">NOSTRUD EXERCITATION</div>
<div class="abs hero-sub">LOREM IPSUM IS DUMMY TEXT ONLY. CONSECTETUR.</div>
<div class="abs arrow" style="left:692px"><svg width="10" height="12" viewBox="0 0 10 12"><path d="M7 1L2 6l5 5" fill="none" stroke="#1d2aa8" stroke-width="2.5"/></svg></div>
<div class="abs arrow" style="left:723px"><svg width="10" height="12" viewBox="0 0 10 12"><path d="M3 1l5 5-5 5" fill="none" stroke="#1d2aa8" stroke-width="2.5"/></svg></div>
<div class="abs dots"><span></span><span class="on"></span><span></span><span></span></div>

<section class="abs welcome">
  <h1>Welcome to Our Website</h1>
  <p>Lorem ipsum dolor sit amet, consectetur adipisicing elit, sed do eiusmod tempor incididunt ut labore et dolore magna aliqua. Ut enim ad minim veniam, quis nostrud exercitation ullamco laboris nisi ut.</p>
  <p>Duis aute irure dolor in reprehenderit in voluptate velit esse cillum dolore eu fugiat nulla pariatur. Excepteur sint occaecat cupidatat non proident, sunt in culpa qui officia deserunt mollit anim id est laborum. Sed ut perspiciatis unde omnis iste natus error sit voluptatem accusantium doloremque laudantium.</p>
</section>

<section class="abs book">
  <div class="book-head">Book a Car</div>
  <div class="abs step" style="left:20px;top:51px">1</div>
  <div class="abs lbl" style="left:56px;top:53px">Pickup Location</div>
  <div class="abs field" style="left:57px;top:72px;width:122px">Enter your location</div>
  <div class="abs step" style="left:20px;top:102px">2</div>
  <div class="abs lbl" style="left:56px;top:104px">Pickup Date</div>
  <div class="abs lbl" style="left:142px;top:104px">Return Date</div>
  <div class="abs field" style="left:57px;top:124px;width:52px"></div>
  <div class="abs field" style="left:142px;top:124px;width:52px"></div>
  <svg class="abs" style="left:94px;top:127px" width="7" height="7" viewBox="0 0 7 7"><rect x=".5" y="1" width="6" height="5.5" fill="none" stroke="#888"/><line x1=".5" y1="2.6" x2="6.5" y2="2.6" stroke="#888"/></svg>
  <svg class="abs" style="left:180px;top:127px" width="7" height="7" viewBox="0 0 7 7"><rect x=".5" y="1" width="6" height="5.5" fill="none" stroke="#888"/><line x1=".5" y1="2.6" x2="6.5" y2="2.6" stroke="#888"/></svg>
  <div class="abs btn" style="left:70px;top:156px;width:98px;height:24px;font-size:11px;line-height:22px">BOOK NOW</div>
</section>

<article class="abs card" style="left:102px">
  <div class="card-photo" role="img" aria-label="White delivery van parked on gravel"></div>
  <h2>VAREBILEN</h2>
  <table class="specs"><tr><td>Pris per døgn</td><td>kr 600</td></tr><tr><td>Biltype</td><td>Varebil</td></tr><tr><td>Maks. pers.</td><td>2</td></tr><tr><td>Ant. dører</td><td>5</td></tr><tr><td>Min. sjåføralder</td><td>21</td></tr><tr><td>Girtype</td><td>Manuell</td></tr><tr><td>Klimaanlegg?</td><td>Ja</td></tr><tr><td>Ubegrenset km?</td><td>Nei</td></tr></table>
  <div class="btn">READ MORE</div>
</article>
<article class="abs card" style="left:358px">
  <div class="card-photo" role="img" aria-label="White delivery van parked on gravel"></div>
  <h2>VAREBILEN</h2>
  <table class="specs"><tr><td>Pris per døgn</td><td>kr 600</td></tr><tr><td>Biltype</td><td>Varebil</td></tr><tr><td>Maks. pers.</td><td>2</td></tr><tr><td>Ant. dører</td><td>5</td></tr><tr><td>Min. sjåføralder</td><td>21</td></tr><tr><td>Girtype</td><td>Manuell</td></tr><tr><td>Klimaanlegg?</td><td>Ja</td></tr><tr><td>Ubegrenset km?</td><td>Nei</td></tr></table>
  <div class="btn">READ MORE</div>
</article>
<article class="abs card" style="left:616px">
  <div class="card-photo" role="img" aria-label="White delivery van parked on gravel"></div>
  <h2>VAREBILEN</h2>
  <table class="specs"><tr><td>Pris per døgn</td><td>kr 600</td></tr><tr><td>Biltype</td><td>Varebil</td></tr><tr><td>Maks. pers.</td><td>2</td></tr><tr><td>Ant. dører</td><td>5</td></tr><tr><td>Min. sjåføralder</td><td>21</td></tr><tr><td>Girtype</td><td>Manuell</td></tr><tr><td>Klimaanlegg?</td><td>Ja</td></tr><tr><td>Ubegrenset km?</td><td>Nei</td></tr></table>
  <div class="btn">READ MORE</div>
</article>

<footer class="abs footer"></footer>
<div class="abs video" role="img" aria-label="Video thumbnail of a red car on a mountain road"></div>
<svg class="abs" style="left:230px;top:1065px" width="20" height="20" viewBox="0 0 20 20"><circle cx="10" cy="10" r="9.5" fill="#fff"/><path d="M8 6l6 4-6 4z" fill="#222"/></svg>
<div class="abs ftxt" style="left:193px;top:1107px;width:110px">Tempor incididunt ut labore et dolore magna aliqua. Ut enim ad minim veniam, quis nostrud exercitation.</div>
<div class="abs ftxt" style="left:193px;top:1138px;width:110px">Ullamco laboris nisi ut aliquip ex ea commodo consequat. Duis aute irure dolo.</div>

<div class="abs fh" style="left:367px">Contact Form</div>
<div class="abs input" style="top:1075px;height:13px">Enter your Email</div>
<div class="abs input" style="top:1092px;height:13px">Subject</div>
<div class="abs input" style="top:1109px;height:35px">Your Message</div>
<div class="abs btn" style="left:367px;top:1150px;width:26px;height:10px;font-size:5px;line-height:9px;font-weight:400;border:0">Submit</div>

<div class="abs fh" style="left:522px">Latest News</div>
<div class="abs news" style="top:1077px"><div class="date"><b>Aug</b>15</div><div class="ftxt" style="font-size:4px;line-height:5.5px;width:84px">Eiusmod tempor incididunt ut labore et dolore magna aliqua. Ut enim ad minim veniam quis nostrud exercitation (Read More)</div></div>
<div class="abs news" style="top:1114px"><div class="date"><b>Aug</b>15</div><div class="ftxt" style="font-size:4px;line-height:5.5px;width:84px">Eiusmod tempor incididunt ut labore et dolore magna aliqua. Ut enim ad minim veniam quis nostrud exercitation (Read More)</div></div>
<div class="abs ftxt" style="left:522px;top:1146px;text-decoration:underline;font-style:italic">View All</div>

<div class="abs fh" style="left:677px">Connect with Us</div>
<div class="abs social" style="top:1075px">Kinnect<i style="background:#3b5998"></i></div>
<div class="abs social" style="top:1091px">Chirpline<i style="background:#1da1f2"></i></div>
<div class="abs social" style="top:1107px">Orbitplus<i style="background:#d34836"></i></div>
<div class="abs social" style="top:1123px">Streamly<i style="background:#d10000"></i></div>

<div class="abs bottom"></div>
<div class="abs bottom-nav"><span>HJEM</span><span>BILPARKEN VÅR</span><span>TJENESTER</span><span>KONTAKT OSS</span><span>BLOG</span><span>ABOUT US</span></div>
<div class="abs copy">Copyright©companyname2014. All Rights Reserved</div>
</body>
</html>
```